Custom Truck shop New Business Card design

double sided business card including my new logo, brand colors and picking a font I attached, clean and modern look. I attached the old card for some reference. and would like to include the picture of the white truck attached. I would also like to have it with one of my employees info as well. (same info except name and title Brin Tolvay Service Writer)

Dale Porvick
Owner

address
48310 E Calloway Ridge Rd S
STE 217
Marsh Hollow, CO 80219

phone 720-555-0184

email dale@brokenspurrigs.example

website brokenspurrgis.example

social @brokenspurrigs

Target Market(s)

men 18-60

Industry/Entity Type

Automotive

Contact Information for Business Card

Dale Porvick Owner address 48310 E Calloway Ridge Rd S STE 217 Marsh Hollow, CO 80219 phone 720-555-0184 email dale@brokenspurrigs.example website brokenspurrgis.example social @brokenspurrigs

Font styles to use
Other font styles liked:
• fonts attached

Requirements
Must have
• new logo, orange #FC68D, Charcoal #333333
Nice to have
• the white truck

```html
<!DOCTYPE html>
<html lang="en">
<head>
<meta charset="utf-8">
<title>Broken Spur Rigs – Business Card</title>
<link href="https://fonts.googleapis.com/css2?family=Fugaz+One&family=Montserrat:ital,wght@0,500;0,600;0,700;1,500&display=swap" rel="stylesheet">
<style>
  :root {
    --bg: #b9bfbf;
    --yellow: #fdd33a;
    --yellow-light: #fee36a;
    --gold: #f0ad1c;
    --charcoal: #2b2d33;
    --charcoal-text: #333333;
    --orange: #fc6d2d;
    --white: #ffffff;
    --photo-sky: #d9dde2;
    --photo-truck: #f2f2f0;
    --photo-ground: #3a3c40;
  }
  * { box-sizing: border-box; margin: 0; padding: 0; }
  html, body { width: 1200px; height: 900px; overflow: hidden; }
  body {
    background: var(--bg);
    font-family: "Montserrat", sans-serif;
    display: flex;
    flex-direction: column;
    align-items: center;
    justify-content: center;
    gap: 60px;
  }
  .card {
    position: relative;
    width: 500px;
    height: 286px;
    overflow: hidden;
    box-shadow: 0 10px 24px rgba(0,0,0,.18);
  }
  .truck-photo {
    position: absolute;
    inset: 0;
    background:
      linear-gradient(180deg, var(--photo-sky) 0%, #c4c9cf 38%, var(--photo-truck) 40%, #dcdcd8 62%, #5a5c62 64%, var(--photo-ground) 100%);
  }

  /* front */
  .card-front { background: var(--yellow); }
  .card-front .truck-photo { clip-path: polygon(64% 0, 100% 0, 100% 100%, 38% 100%); }
  .front-shapes { position: absolute; inset: 0; }
  .brand {
    position: absolute;
    left: 40px;
    top: 96px;
    display: flex;
    align-items: center;
    gap: 10px;
  }
  .brand-dot {
    width: 22px; height: 22px;
    border-radius: 50%;
    background: var(--orange);
  }
  .brand-name {
    font-weight: 700;
    font-size: 20px;
    letter-spacing: .06em;
    color: var(--charcoal-text);
    text-transform: uppercase;
  }
  .front-website {
    position: absolute;
    left: 26px;
    bottom: 13px;
    font-size: 13px;
    font-weight: 600;
    color: var(--charcoal-text);
  }
  .front-website b { font-weight: 700; margin-right: 4px; }

  /* back */
  .card-back { background: var(--charcoal); color: var(--white); }
  .card-back .truck-photo { clip-path: polygon(78% 0, 100% 0, 100% 100%, 48% 100%); }
  .back-shapes { position: absolute; inset: 0; }
  .person { position: absolute; left: 34px; top: 24px; }
  .person-name {
    font-family: "Fugaz One", sans-serif;
    font-size: 25px;
    color: var(--white);
    padding-bottom: 3px;
    border-bottom: 2px solid var(--white);
    display: inline-block;
  }
  .person-title {
    font-size: 13px;
    font-style: italic;
    font-weight: 500;
    color: var(--yellow);
    margin-top: 2px;
  }
  .contact {
    position: absolute;
    left: 34px;
    top: 108px;
    list-style: none;
    font-size: 10.5px;
    line-height: 1.35;
  }
  .contact li { display: flex; gap: 10px; align-items: flex-start; margin-bottom: 7px; }
  .contact svg { width: 13px; height: 13px; flex: none; fill: var(--yellow); margin-top: 1px; }
  .contact .address { font-weight: 700; }
  .contact .phone { font-style: italic; }
  .social {
    position: absolute;
    left: 30px;
    bottom: 9px;
    display: flex;
    align-items: center;
    gap: 6px;
    font-size: 12px;
    font-weight: 600;
    color: var(--charcoal-text);
  }
  .social-dot { width: 12px; height: 12px; border-radius: 50%; background: var(--charcoal); }
</style>
</head>
<body>

  <!-- Front -->
  <section class="card card-front" aria-label="Business card front">
    <div class="truck-photo" role="img" aria-label="Photo of a lifted white pickup truck in a parking lot"></div>
    <svg class="front-shapes" viewBox="0 0 500 286" preserveAspectRatio="none" aria-hidden="true">
      <polygon points="248,286 360,140 400,286" fill="var(--yellow-light)"/>
      <polygon points="0,246 300,246 270,286 0,286" fill="var(--gold)"/>
    </svg>
    <div class="brand">
      <span class="brand-dot"></span>
      <span class="brand-name">Broken Spur Rigs</span>
    </div>
    <p class="front-website"><b>website</b> brokenspurrgis.example</p>
  </section>

  <!-- Back -->
  <section class="card card-back" aria-label="Business card back">
    <div class="truck-photo" role="img" aria-label="Photo of a lifted white pickup truck from the side"></div>
    <svg class="back-shapes" viewBox="0 0 500 286" preserveAspectRatio="none" aria-hidden="true">
      <polygon points="0,252 264,252 244,286 0,286" fill="var(--gold)"/>
    </svg>
    <div class="person">
      <h1 class="person-name">Dale Porvick</h1>
      <p class="person-title">Owner</p>
    </div>
    <ul class="contact">
      <li>
        <svg viewBox="0 0 16 16"><path d="M8 1 1 7h2v8h4v-5h2v5h4V7h2z"/></svg>
        <span class="address">48310 E Calloway Ridge Rd S<br>STE 217 Marsh Hollow, CO 80219</span>
      </li>
      <li>
        <svg viewBox="0 0 16 16"><path d="M4 1 1.5 3.5c0 6 5 11 11 11L15 12l-3-3-2 1.5C8 9.5 6.5 8 5.5 6L7 4z"/></svg>
        <span class="phone">Office : 720-555-0184</span>
      </li>
      <li>
        <svg viewBox="0 0 16 16"><path d="M1 3h14v10H1zM2 4l6 5 6-5v-.5H2z"/></svg>
        <span>dale@brokenspurrigs.example</span>
      </li>
      <li>
        <svg viewBox="0 0 16 16"><path d="M8 1a7 7 0 1 0 0 14A7 7 0 0 0 8 1zm0 1.5c.8.9 1.4 2.3 1.6 4H6.4C6.6 4.8 7.2 3.4 8 2.5zM2.6 7.5h2.3c.1 1.6.5 3 1.1 4A5.5 5.5 0 0 1 2.6 7.5zm4.8 0h2.2c-.2 1.6-.8 3-1.6 4-.8-1-1.4-2.4-1.6-4zm3.7 0h2.3A5.5 5.5 0 0 1 10 11.5c.6-1 1-2.4 1.1-4z"/></svg>
        <span>www.brokenspurrgis.example</span>
      </li>
    </ul>
    <p class="social">
      <span class="social-dot"></span>
      <span>social @brokenspurrigs</span>
    </p>
  </section>

</body>
</html>
```